Marrow Creek 381 Wine Label

Marrow Creek 381 Wine bottle label-
Pinot Noir, Chardonnay. Premium label.
Startup vineyard, Cool climate, Tasmania Australia.
Hills and Valley area, South East location
Needs to be a front and rear label as there are label requirements in Australia. Rear lable
is mearly to talk about the wine and have required information as per the examples uploaded

```html
<!DOCTYPE html>
<html lang="en">
<head>
<meta charset="UTF-8">
<title>Marrow Creek 381 – Wine Label</title>
<link rel="stylesheet" href="https://fonts.googleapis.com/css2?family=EB+Garamond:wght@400;500&display=swap">
<style>
  :root {
    --page: #ffffff;
    --label: #0f0c08;
    --gold: #c9a46a;
    --white: #f1ede6;
    --grey: #9a958d;
    --divider: #8d8475;
    --red: #cf1820;
    --seal: #a3161b;
  }
  * { margin: 0; padding: 0; box-sizing: border-box; }
  html, body {
    width: 1200px;
    height: 1200px;
    overflow: hidden;
    background: var(--page);
    font-family: "EB Garamond", Georgia, serif;
  }
  .canvas { position: relative; width: 1200px; height: 1200px; }

  .label {
    position: absolute;
    left: 100px;
    width: 1000px;
    background: var(--label);
    border-radius: 10px;
  }
  .label--front { top: 225px; height: 502px; }
  .label--band { top: 744px; height: 231px; }

  .brand {
    position: absolute;
    right: 580px;
    top: 182px;
    text-align: right;
    color: var(--gold);
    font-weight: 400;
    text-transform: uppercase;
    line-height: 1;
  }
  .brand__line { display: block; font-size: 50px; letter-spacing: 0.02em; }
  .brand__line--number { font-size: 92px; margin-top: 2px; }

  .front__divider {
    position: absolute;
    left: 435px;
    top: 178px;
    width: 1.5px;
    height: 186px;
    background: var(--divider);
  }
  .details {
    position: absolute;
    left: 451px;
    top: 194px;
    color: var(--white);
  }
  .details__variety { font-size: 43px; line-height: 1; letter-spacing: 0.01em; }
  .details__variety .soft { color: #d6d1c8; }
  .details__vintage { font-size: 42px; line-height: 1; margin-top: 16px; }
  .details__spec { font-size: 20px; line-height: 1.3; margin-top: 6px; color: #cfcac2; }

  .seal {
    position: absolute;
    left: 140px;
    top: 54px;
    width: 122px;
    height: 122px;
    border-radius: 50%;
    background: radial-gradient(circle at 40% 35%, #c8262b, var(--seal) 60%, #7e0f13);
  }
  .origin {
    position: absolute;
    left: 290px;
    top: 68px;
  }
  .origin__intro { font-size: 28px; line-height: 1; color: var(--white); }
  .origin__intro .soft { color: var(--grey); }
  .origin__place {
    font-size: 27px;
    line-height: 1;
    margin-top: 13px;
    margin-left: 10px;
    color: var(--red);
    font-weight: 500;
    letter-spacing: 0.18em;
  }
  .origin__number {
    font-size: 20px;
    line-height: 1;
    margin-top: 14px;
    margin-left: 130px;
    color: var(--grey);
  }
</style>
</head>
<body>
<main class="canvas">
  <section class="label label--front">
    <h1 class="brand">
      <span class="brand__line">Marrow Creek</span>
      <span class="brand__line brand__line--number">381</span>
    </h1>
    <div class="front__divider"></div>
    <div class="details">
      <p class="details__variety">Pinot Noir <span class="soft">&amp; Chardonnay</span></p>
      <p class="details__vintage">2025</p>
      <p class="details__spec">750 ml<br>12% Vol.</p>
    </div>
  </section>

  <section class="label label--band">
    <div class="seal" role="img" aria-label="Red wax seal"></div>
    <div class="origin">
      <p class="origin__intro">This Beautiful <span class="soft">Wine was</span> Created In:</p>
      <p class="origin__place">TASMANIA, AUSTRALIA</p>
      <p class="origin__number">Bottle No.: 1/500</p>
    </div>
  </section>
</main>
</body>
</html>
```